Design Tweak needed for a current site

Design on top of an existing quiz funnel

Ideally we would like to tweak what we have already built here (moving elements, styles, adding simple elements etc): http://offers.plumrivetdeals.com/can-you-save-on-car-insurance

The flow:
1) User lands on the quiz page
2) User answers X questions and moves through the flow
3) Calculating user results screen
4) User reaches a success screen, and is subsequently redirected

Keys to the design:
1) We need to emphasize the quiz title as that will drive engagement. In this case, this is a quiz to see if you might be eligible to save money on car insurance.

2) At the end of the quiz we need to make it very, very clear that the user is eligible for savings and that in order to complete the process they are being redirected to another page where they need to fill out a form. It is critical that the design communicates this very clearly... We can count down the time left until redirect and we can use any order of elements to make this point. I think our current design does a very bad job of this.

3) We want to have a "calculating" step so that it seems like the page is working in the background

Goals of the design:
1) Polished, high quality experience throughout
2) User is clearly prepared to be redirected to the conversion funnel/landing page at the end
3) User understands the value of completing the quiz

Target Market(s)

designers

Industry/Entity Type

Moving

Number of Pages Required

1 page

Font styles to use
Sans Serif

Colors

Designer to choose colors to be used in the design.

Requirements
Must have
• This quiz funnel is a template so while the current use case is for auto insurance, we would like a design that also would work in other contexts.
Should not have
• We don't want to materially change the core functionality of the quiz itself... redesigning any of the elements or interactions is encouraged though

```html
<!DOCTYPE html>
<html lang="en">
<head>
<meta charset="utf-8">
<title>Quiz Result – PlumRivetDeals</title>
<link rel="stylesheet" href="https://fonts.googleapis.com/css2?family=Open+Sans:wght@300;400;600;700&display=swap">
<style>
  :root {
    --page-bg: #ffffff;
    --header-bg: #e8e8e8;
    --ink: #333333;
    --ink-soft: #555555;
    --card-border: #d8d8d8;
    --accent-blue: #1a76d2;
    --accent-blue-soft: #e3eefa;
    --success-green: #3cb13c;
    --white: #ffffff;
  }
  * { box-sizing: border-box; margin: 0; padding: 0; }
  html, body {
    width: 1200px;
    height: 701px;
    overflow: hidden;
    background: var(--page-bg);
    font-family: "Open Sans", Arial, sans-serif;
    color: var(--ink);
  }
  .site-header {
    position: absolute;
    left: 0; top: 0;
    width: 1200px;
    height: 70px;
    background: var(--header-bg);
    display: flex;
    align-items: center;
    justify-content: center;
  }
  .brand {
    display: flex;
    align-items: center;
    gap: 10px;
    font-size: 29px;
    font-weight: 600;
    color: #222222;
  }
  .brand-dot {
    width: 30px;
    height: 30px;
    border-radius: 50%;
    background: #222222;
  }
  .quiz-card {
    position: absolute;
    left: 23px; top: 102px;
    width: 1154px;
    height: 561px;
    border: 1px solid var(--card-border);
  }
  .quiz-title {
    position: absolute;
    left: 23px; top: 30px;
    font-size: 23px;
    font-weight: 700;
    letter-spacing: 0.5px;
    white-space: nowrap;
  }
  .quiz-subtitle {
    position: absolute;
    left: 23px; top: 67px;
    font-size: 15px;
    letter-spacing: 0.25px;
    white-space: nowrap;
  }
  .title-rule {
    position: absolute;
    left: 26px; top: 117px;
    width: 48px;
    height: 3px;
    background: var(--accent-blue);
  }
  .result-heading {
    position: absolute;
    left: 21px; top: 152px;
    display: flex;
    align-items: center;
    gap: 22px;
  }
  .result-heading svg { width: 48px; height: 48px; display: block; }
  .result-heading h2 {
    font-size: 48px;
    font-weight: 300;
    letter-spacing: 1px;
    line-height: 60px;
    white-space: nowrap;
  }
  .result-note {
    position: absolute;
    left: 23px; top: 216px;
    font-size: 15.5px;
    letter-spacing: 0.3px;
    white-space: nowrap;
  }
  .redirect-notice {
    position: absolute;
    left: 23px; top: 256px;
    width: 1000px;
    padding: 0 0 0 16px;
    border-left: 4px solid var(--accent-blue);
  }
  .next-step {
    font-size: 19.5px;
    font-weight: 600;
    line-height: 30px;
    color: var(--ink);
    white-space: nowrap;
  }
  .countdown {
    margin-top: 12px;
    font-size: 20px;
    font-weight: 400;
    line-height: 28px;
    color: var(--accent-blue);
  }
  .countdown-number { font-weight: 700; }
  .countdown-track {
    margin-top: 12px;
    width: 420px;
    height: 6px;
    border-radius: 3px;
    background: var(--accent-blue-soft);
  }
  .countdown-fill {
    width: 35%;
    height: 6px;
    border-radius: 3px;
    background: var(--accent-blue);
  }
  .reset-button {
    position: absolute;
    left: 464px; top: 463px;
    width: 187px;
    height: 46px;
    border: 0;
    background: var(--accent-blue);
    color: var(--white);
    font-family: "Open Sans", Arial, sans-serif;
    font-size: 14px;
    font-weight: 600;
  }
</style>
</head>
<body>
  <header class="site-header">
    <div class="brand">
      <span class="brand-dot"></span>
      <span class="brand-name">PlumRivetDeals</span>
    </div>
  </header>

  <main class="quiz-card">
    <h1 class="quiz-title">QUIZ: ARE YOU OVERPAYING FOR CAR INSURANCE ?</h1>
    <p class="quiz-subtitle">TAKE OUR FIVE QUESTION QUIZ TO SEE IF YOU MIGHT BE ELIGIBLE FOR CAR INSURANCE SAVINGS</p>
    <div class="title-rule"></div>

    <div class="result-heading">
      <svg viewBox="0 0 48 48" aria-hidden="true">
        <circle cx="24" cy="24" r="24" fill="var(--success-green)"/>
        <path d="M14 25 L21 32 L34 17" fill="none" stroke="#ffffff" stroke-width="4" stroke-linecap="round" stroke-linejoin="round"/>
      </svg>
      <h2>CONGRATULATIONS</h2>
    </div>
    <p class="result-note">YOU ARE LIKELY ELIGIBLE FOR THE SAVINGS !</p>

    <section class="redirect-notice">
      <p class="next-step">As a next step complete our forum on next page to get a quote to beat your auto insurance premiums !</p>
      <p class="countdown">Redirecting in <span class="countdown-number">5</span> seconds...</p>
      <div class="countdown-track"><div class="countdown-fill"></div></div>
    </section>

    <button class="reset-button" type="button">Reset and Start New</button>
  </main>
</body>
</html>
```